Customs House descriptive business cards

We require a two-sided business card that has a simple yet elegant design. We want to be able to promote our services as a customs house. This card should include our logo, contact info and services offered with the logo being on one side and the contact info and services on the flip side

Target Market(s)

Importers / exporters to and from the Bahamas

Industry/Entity Type

Logistics

Contact Information for Business Card

The front side of the card could have the logo and the flip side should have the other relevant info

Font styles to use
Serif

Colors

Designer to choose colors to be used in the design.

Requirements
Must have
• (Harbourline Agents Ltd) Logo, address and contact info also services:
• import customs clearance, Delivery & HAndling services,Florida pickups, Export packing & Crating Services, export customs clearance, Consulting

```html
<!DOCTYPE html>
<html lang="en">
<head>
<meta charset="UTF-8">
<title>Harbourline Agents Ltd — Business Cards</title>
<link rel="stylesheet" href="https://fonts.googleapis.com/css2?family=Montserrat:wght@400;500;600;700&display=swap">
<style>
  :root {
    --brand-blue: #3380b9;
    --brand-blue-dark: #2a6fa3;
    --card-white: #f3f3f3;
    --ink: #4a4a4a;
    --ink-soft: #6a6a6a;
    --rule: #b9b9b9;
    --backdrop: #ececec;
  }
  * { margin: 0; padding: 0; box-sizing: border-box; }
  html, body {
    width: 1200px; height: 1134px; overflow: hidden;
    background: var(--backdrop);
    font-family: "Montserrat", sans-serif;
  }
  .canvas { position: relative; width: 1200px; height: 1134px; }

  .card {
    position: absolute;
    width: 600px; height: 343px;
    box-shadow: 0 6px 18px rgba(0,0,0,0.10);
    overflow: hidden;
  }

  /* Front: logo side */
  .card--front {
    left: 540px; top: 150px;
    background: var(--brand-blue);
    display: flex; align-items: center; justify-content: center;
  }
  .brand {
    display: flex; align-items: center; gap: 14px;
    font-weight: 600; letter-spacing: 0.04em;
  }
  .brand__mark { width: 22px; height: 22px; border-radius: 50%; }
  .card--front .brand { color: #ffffff; font-size: 30px; }
  .card--front .brand__mark { background: #ffffff; }

  /* Back: contact and services side */
  .card--back {
    left: 60px; top: 600px;
    background: var(--card-white);
  }
  .card__body {
    position: absolute; left: 0; top: 0; right: 0; height: 262px;
    display: flex; align-items: center;
  }
  .card__logo-area {
    width: 300px; display: flex; justify-content: center;
  }
  .card--back .brand { color: var(--brand-blue); font-size: 17px; gap: 10px; }
  .card--back .brand__mark { width: 14px; height: 14px; background: var(--brand-blue); }
  .card__divider {
    width: 1px; height: 120px; background: var(--rule);
  }
  .contact { padding-left: 26px; color: var(--ink-soft); font-size: 12px; line-height: 1.45; }
  .contact__name { color: var(--ink); font-size: 18px; font-weight: 700; line-height: 1.1; }
  .contact__title { margin-bottom: 6px; font-size: 12.5px; }
  .contact__address { margin-bottom: 8px; }
  .contact__list { list-style: none; }
  .contact__item { display: flex; align-items: center; gap: 8px; }
  .contact__icon { width: 11px; height: 11px; flex: none; }

  .services {
    position: absolute; left: 0; right: 0; bottom: 0; height: 81px;
    background: var(--brand-blue);
    color: #ffffff; font-size: 12.5px; font-weight: 500; letter-spacing: 0.02em;
    line-height: 1.6; padding: 16px 26px;
  }
</style>
</head>
<body>
<main class="canvas">

  <section class="card card--front" aria-label="Card front">
    <div class="brand"><span class="brand__mark"></span>Harbourline Agents Ltd.</div>
  </section>

  <section class="card card--back" aria-label="Card back">
    <div class="card__body">
      <div class="card__logo-area">
        <div class="brand"><span class="brand__mark"></span>Harbourline Agents Ltd.</div>
      </div>
      <div class="card__divider"></div>
      <div class="contact">
        <p class="contact__name">Daniel REYES</p>
        <p class="contact__title">Managing Director</p>
        <p class="contact__address">412 Quayside Road East<br>Port Elgin ON, Canada, N0H 2C0</p>
        <ul class="contact__list">
          <li class="contact__item">
            <svg class="contact__icon" viewBox="0 0 12 12"><path d="M3 1 L5 3.5 L4 5 Q5 7 7 8 L8.5 7 L11 9 L9.5 11 Q4 10.5 1 3 Z" fill="#6a6a6a"/></svg>
            000.000.0000
          </li>
          <li class="contact__item">
            <svg class="contact__icon" viewBox="0 0 12 12"><rect x="3" y="1" width="6" height="10" rx="1" fill="none" stroke="#6a6a6a" stroke-width="1.2"/></svg>
            000.000.0000
          </li>
          <li class="contact__item">
            <svg class="contact__icon" viewBox="0 0 12 12"><rect x="1" y="2.5" width="10" height="7" fill="none" stroke="#6a6a6a" stroke-width="1.1"/><path d="M1 2.5 L6 6.5 L11 2.5" fill="none" stroke="#6a6a6a" stroke-width="1.1"/></svg>
            daniel@harbourlineagents.com
          </li>
          <li class="contact__item">
            <svg class="contact__icon" viewBox="0 0 12 12"><circle cx="6" cy="6" r="5" fill="none" stroke="#6a6a6a" stroke-width="1.1"/><ellipse cx="6" cy="6" rx="2.2" ry="5" fill="none" stroke="#6a6a6a" stroke-width="0.9"/><path d="M1 6 H11" stroke="#6a6a6a" stroke-width="0.9"/></svg>
            www.harbourlineagents.com
          </li>
        </ul>
      </div>
    </div>
    <div class="services">
      Import Customs Clearance, Delivery &amp; Handling Services, Florida Pickups<br>
      Export Packing &amp; Crating Services, Export Customs Clearance, Consulting
    </div>
  </section>

</main>
</body>
</html>
```